Modern, corporate management consultancy firm needs a new website

We need a website for an Australian based management consultancy firm.

The company name is Norcott Strategy Partners.

We are looking for a parallax style wordpress site.

The site needs to provide the following functions:

1) subscribe function
2) links to social media (twitter, linkedin and mail)
3) a gated document section where people can download pdf's from the site after registering or providing name, company, position, email and contact number.

Attached is the company logo, would like to see designs that incorporate the dark blue and silver in the logo and separated into the following sections (Home, About, Services (with 4 options), Our Team, Links, Contacts.

Need the site to be easy to navigate and updated.

Potentially a News Section that can be updated regularly.

Target Market(s)

Target market is SME, business owners and directors

Industry/Entity Type

Management Consulting

Coding

Coded - Design and coding required

Number of Pages Required

1 page

Font styles to use
Sans Serif

Colors
0255a3
cbcbcb
757575
000000

Requirements
Must have
• Must be easy to read and use
Nice to have
• Features are listed on initial brief

```html
<!DOCTYPE html>
<html lang="en">
<head>
<meta charset="utf-8">
<title>Norcott Strategy Partners</title>
<link href="https://fonts.googleapis.com/css2?family=Montserrat:wght@300;400;600&family=Open+Sans:wght@400;600&display=swap" rel="stylesheet">
<style>
:root{
  --blue:#0255a3;
  --silver:#cbcbcb;
  --grey:#757575;
  --black:#000000;
  --ink:#333a40;
  --light:#f4f5f6;
  --white:#ffffff;
  --dark:#26292c;
  --red:#e2464a;
}
*{box-sizing:border-box;margin:0;padding:0}
html,body{width:1200px;height:2828px;overflow:hidden}
body{font-family:"Open Sans",Arial,sans-serif;color:var(--grey);background:var(--white);font-size:12px;line-height:1.6}
.section-title{font-family:"Montserrat",Arial,sans-serif;font-weight:300;font-size:30px;letter-spacing:2px;text-transform:uppercase;color:var(--ink);text-align:center}
.section-intro{width:560px;margin:14px auto 0;text-align:center;font-size:11px;line-height:1.7;color:var(--grey)}
.btn{display:inline-block;font-family:"Montserrat",Arial,sans-serif;font-size:10px;font-weight:600;letter-spacing:1px;text-transform:uppercase;text-decoration:none;padding:9px 22px;color:var(--white)}

/* header + hero */
.hero{position:relative;height:450px;background:linear-gradient(115deg,#c9ced3 0%,#9ea6ae 35%,#6e757c 60%,#b8bec4 100%)}
.hero::after{content:"";position:absolute;inset:0;background:rgba(0,0,0,.18)}
.site-header{position:absolute;top:0;left:0;right:0;height:64px;background:rgba(255,255,255,.95);display:flex;align-items:center;justify-content:space-between;padding:0 232px;z-index:2}
.brand{display:flex;align-items:center;gap:10px;font-family:"Montserrat",Arial,sans-serif;font-weight:600;font-size:13px;color:var(--blue)}
.brand-dot{width:26px;height:26px;border-radius:50%;background:var(--blue)}
.main-nav{display:flex;align-items:center;gap:30px}
.main-nav a{font-family:"Montserrat",Arial,sans-serif;font-size:10px;text-transform:uppercase;letter-spacing:1px;color:var(--ink);text-decoration:none}
.main-nav a.active{color:var(--blue);border-bottom:2px solid var(--blue);padding-bottom:4px}
.main-nav a.nav-contact{border:1px solid var(--blue);color:var(--blue);padding:6px 16px}
.hero-copy{position:absolute;z-index:2;left:0;right:0;top:200px;text-align:center;color:var(--white)}
.hero-copy h1{font-family:"Montserrat",Arial,sans-serif;font-weight:300;font-size:40px}
.hero-copy p{width:520px;margin:10px auto 0;font-size:12px}

/* about */
.about{height:370px;background:var(--light);padding-top:60px}
.about-cols{display:flex;justify-content:center;gap:90px;margin-top:46px}
.about-col{width:220px;text-align:center}
.about-col svg{display:block;margin:0 auto 10px}
.about-col h3{font-family:"Montserrat",Arial,sans-serif;font-size:11px;font-weight:600;color:var(--ink);letter-spacing:1px;text-transform:uppercase}
.about-col p{font-size:10px;margin:6px 0 12px}
.btn-small{font-size:9px;padding:5px 14px;background:var(--blue)}

/* services */
.services{height:380px;padding-top:60px}
.service-tiles{display:flex;margin-top:44px}
.service-tile{position:relative;width:300px;height:180px}
.service-tile span{position:absolute;top:14px;left:0;right:0;text-align:center;color:var(--white);font-family:"Montserrat",Arial,sans-serif;font-size:14px}
.tile-1{background:linear-gradient(135deg,#8a929a,#c2c8cd)}
.tile-2{background:linear-gradient(135deg,#5e666e,#9aa2a9)}
.tile-3{background:linear-gradient(135deg,#0255a3,#3d7fc0)}
.tile-4{background:linear-gradient(135deg,#4d545b,#8d959c)}

/* news */
.news{height:420px;padding-top:44px}
.news-grid{display:flex;justify-content:center;gap:24px;margin-top:26px}
.news-card{width:165px}
.news-image{position:relative;height:96px}
.news-date{position:absolute;top:0;left:0;width:32px;height:32px;background:var(--blue);color:var(--white);font-size:9px;line-height:1.1;text-align:center;padding-top:5px;font-weight:600}
.news-date b{display:block;font-size:13px}
.news-card h4{margin-top:10px;font-family:"Montserrat",Arial,sans-serif;font-size:9px;font-weight:600;color:var(--blue);text-transform:uppercase;letter-spacing:.5px}
.news-card p{font-size:9px;line-height:1.5;margin-top:4px}
.img-a{background:linear-gradient(135deg,#2d3136,#7e868d)}
.img-b{background:linear-gradient(135deg,#c7ccd0,#8d949a)}
.img-c{background:linear-gradient(135deg,#e3e5e7,#a9afb4)}
.img-d{background:linear-gradient(135deg,#d9b46a,#6f7780)}

/* downloads */
.downloads{height:290px;background:linear-gradient(120deg,#1d2023,#3a3f44 50%,#222528);padding-top:60px;text-align:center}
.downloads .section-title{color:var(--white)}
.downloads .section-intro{color:var(--silver)}
.download-actions{margin-top:24px;display:flex;justify-content:center;gap:14px}
.btn-blue{background:var(--blue)}
.btn-red{background:var(--red)}

/* team */
.team{height:530px;padding-top:60px}
.team-grid{display:flex;justify-content:center;gap:24px;margin-top:36px}
.team-member{width:208px;text-align:center}
.team-photo{height:200px}
.photo-1{background:linear-gradient(135deg,#dfe8ea,#9fb4b8)}
.photo-2{background:linear-gradient(135deg,#4a5058,#a5adb4)}
.photo-3{background:linear-gradient(135deg,#e7e4df,#b3aca4)}
.team-member h4{margin-top:14px;font-family:"Montserrat",Arial,sans-serif;font-size:10px;font-weight:600;color:var(--ink);text-transform:uppercase}
.team-member p{font-size:9px;color:var(--blue);text-transform:uppercase;letter-spacing:.5px}

/* social */
.social{height:330px;background:linear-gradient(110deg,#2a2d30,#55595e 45%,#303337);padding-top:70px;text-align:center}
.social .section-title{color:var(--white);font-size:22px}
.social .section-intro{color:var(--silver)}
.social-links{display:flex;justify-content:center;gap:14px;margin-top:30px}
.social-links a{width:30px;height:30px;border-radius:50%;background:var(--silver);display:flex;align-items:center;justify-content:center}

.site-footer{height:48px;line-height:48px;text-align:center;font-size:9px;color:var(--grey);background:var(--white)}
</style>
</head>
<body>

<section class="hero" role="img" aria-label="Photo of three business professionals reviewing a tablet in an office">
  <header class="site-header">
    <div class="brand"><span class="brand-dot"></span>Norcott Strategy Partners</div>
    <nav class="main-nav">
      <a href="#" class="active">Home</a>
      <a href="#">About Us</a>
      <a href="#">Services</a>
      <a href="#">Our Team</a>
      <a href="#">Links</a>
      <a href="#" class="nav-contact">Contacts</a>
    </nav>
  </header>
  <div class="hero-copy">
    <h1>Business Improvement Specialists</h1>
    <p>Practical strategy and performance advice for business owners and directors, helping growing firms run leaner and plan with confidence.</p>
  </div>
</section>

<section class="about">
  <h2 class="section-title">We Are Norcott</h2>
  <p class="section-intro">We partner with small and medium enterprises across Australia, delivering clear plans, honest insight and measurable results that help leadership teams build stronger, more profitable businesses.</p>
  <div class="about-cols">
    <div class="about-col">
      <svg width="26" height="26" viewBox="0 0 26 26" fill="none" stroke="#0255a3" stroke-width="1.5"><circle cx="13" cy="13" r="11"/><path d="M8 13l4 4 6-8"/></svg>
      <h3>Strategy</h3>
      <p>Focused plans built around your goals and market.</p>
      <a class="btn btn-small" href="#">Read More</a>
    </div>
    <div class="about-col">
      <svg width="26" height="26" viewBox="0 0 26 26" fill="none" stroke="#0255a3" stroke-width="1.5"><path d="M3 22h20M6 20v-6M12 20V9M18 20V4"/></svg>
      <h3>Business Improvement</h3>
      <p>Lift performance with sharper systems and processes.</p>
      <a class="btn btn-small" href="#">Read More</a>
    </div>
    <div class="about-col">
      <svg width="26" height="26" viewBox="0 0 26 26" fill="none" stroke="#0255a3" stroke-width="1.5"><rect x="3" y="6" width="20" height="14"/><path d="M3 6l10 8 10-8"/></svg>
      <h3>Subscribe</h3>
      <p>Receive our latest insights straight to your inbox.</p>
      <a class="btn btn-small" href="#">Sign Up</a>
    </div>
  </div>
</section>

<section class="services">
  <h2 class="section-title">Our Services</h2>
  <p class="section-intro">Four core services designed for owners and directors who want a clear view of where their business stands and a practical path to where it should be next.</p>
  <div class="service-tiles">
    <div class="service-tile tile-1" role="img" aria-label="Photo of a consultant working at a laptop"><span>Business Health Check</span></div>
    <div class="service-tile tile-2" role="img" aria-label="Photo of a team meeting around a desk"><span>Business Performance Consulting</span></div>
    <div class="service-tile tile-3" role="img" aria-label="Photo of financial reports on a desk, tinted blue"><span>Financial Management</span></div>
    <div class="service-tile tile-4" role="img" aria-label="Photo of a manager reviewing documents"><span>Management Performance Review</span></div>
  </div>
</section>

<section class="news">
  <h2 class="section-title">Recent News</h2>
  <p class="section-intro">Updates, articles and commentary from our advisers on the issues shaping Australian small and medium businesses today.</p>
  <div class="news-grid">
    <article class="news-card">
      <div class="news-image img-a" role="img" aria-label="Photo of a person walking past office windows"><div class="news-date"><b>12</b>MAR</div></div>
      <h4>Management Consultancy</h4>
      <p>How clear reporting helps directors make faster decisions.</p>
    </article>
    <article class="news-card">
      <div class="news-image img-b" role="img" aria-label="Photo of colleagues in discussion"><div class="news-date"><b>08</b>MAR</div></div>
      <h4>Management Consultancy</h4>
      <p>Five signs your business is ready for its next stage.</p>
    </article>
    <article class="news-card">
      <div class="news-image img-c" role="img" aria-label="Photo of a coffee cup beside a notebook"><div class="news-date"><b>02</b>MAR</div></div>
      <h4>Management Consultancy</h4>
      <p>Planning cash flow through a slower trading season.</p>
    </article>
    <article class="news-card">
      <div class="news-image img-d" role="img" aria-label="Photo of a desk with charts and a laptop"><div class="news-date"><b>24</b>FEB</div></div>
      <h4>Management Consultancy</h4>
      <p>Building a leadership team that can run without you.</p>
    </article>
  </div>
</section>

<section class="downloads">
  <h2 class="section-title">Download PDFs</h2>
  <p class="section-intro">Access our guides, checklists and reports. Register once with your name, company, position, email and contact number to unlock the full document library.</p>
  <div class="download-actions">
    <a class="btn btn-blue" href="#">Register Now</a>
    <a class="btn btn-red" href="#">Download</a>
  </div>
</section>

<section class="team">
  <h2 class="section-title">Meet The Team</h2>
  <p class="section-intro">Experienced advisers with backgrounds in finance, operations and leadership, working side by side with our clients.</p>
  <div class="team-grid">
    <div class="team-member">
      <div class="team-photo photo-1" role="img" aria-label="Portrait photo of a female adviser"></div>
      <h4>Clara Henley</h4>
      <p>Financial Adviser</p>
    </div>
    <div class="team-member">
      <div class="team-photo photo-2" role="img" aria-label="Portrait photo of a male director"></div>
      <h4>Marcus Doyle</h4>
      <p>Managing Director</p>
    </div>
    <div class="team-member">
      <div class="team-photo photo-3" role="img" aria-label="Portrait photo of a male consultant"></div>
      <h4>Peter Lindqvist</h4>
      <p>Senior Consultant</p>
    </div>
  </div>
</section>

<section class="social">
  <h2 class="section-title">Social Media</h2>
  <p class="section-intro">Follow us for news, events and practical business advice, or send us a message and our team will be in touch.</p>
  <div class="social-links">
    <a href="#" aria-label="Follow us"></a>
    <a href="#" aria-label="Connect with us"></a>
    <a href="#" aria-label="Email us"><svg width="14" height="10" viewBox="0 0 14 10" fill="none" stroke="#26292c" stroke-width="1.2"><rect x=".6" y=".6" width="12.8" height="8.8"/><path d="M.6.6L7 5.5 13.4.6"/></svg></a>
  </div>
</section>

<footer class="site-footer">© Copyright 2024 Norcott Strategy Partners. All Rights Reserved.</footer>

</body>
</html>
```